Business cards for investing fund

I need processional luxury classical business cards for CEO of the investing company. I need it to be elegant. I need it to look expensive. It will be printed o fine paper with UV. I prefer light and minimalistic design. Logo of my company must be included at least on front page.

Target Market(s)

40+ investors

Industry/Entity Type

Finance And Accounting

Contact Information for Business Card

FRONT PAGE:

Wiktor Osmalek
President & CEO

e: vik@brlcap.example
w: www.brlcap.example
p: +44 20 7395 2847
m: +44 75 2918 3406

Brass Lark Venture Capital, LLC
17 W Pinecrest Ave., Sheridan, WY 82801
Filling number: 2019-000542319

BACK PAGE (with or without logo):

PROUD GROUP MEMBERS:

UK: Marrow Bay Associates Ltd. | 42 Elmsworth Row, 1st fl. | W1T-4QR London
PL: Marrow Bay Trust S.A. | ul. Lipowa Polna 14, 4p. | 00-871 Warszawa
US: Crestfall Advisors, LLC | 213 Orchard Lane, Suite 409, NYC | 10017 New York

Font styles to use
Serif
Sans Serif
Decorative

Colors
0355a3
ec1f27

Requirements
Must have
• My own logo (attached)

```html
<!DOCTYPE html>
<html lang="en">
<head>
<meta charset="utf-8">
<title>Brass Lark Venture Capital — Business Cards</title>
<link href="https://fonts.googleapis.com/css2?family=EB+Garamond:wght@400;600;700&display=swap" rel="stylesheet">
<style>
  :root {
    --backdrop: #3a2e26;
    --card: #161616;
    --card-edge: #0b0b0b;
    --ink: #f2f2f2;
    --ink-soft: #d6d6d6;
    --name-silver: #b4b4b4;
    --name-faint: #2a2a2a;
  }
  * { margin: 0; padding: 0; box-sizing: border-box; }
  html, body { width: 1200px; height: 715px; overflow: hidden; }
  body {
    background: var(--backdrop);
    font-family: "EB Garamond", Georgia, serif;
    color: var(--ink);
    position: relative;
  }
  .card {
    position: absolute;
    top: 190px;
    width: 520px;
    height: 335px;
    background: var(--card);
    box-shadow: 0 2px 0 var(--card-edge), 0 14px 30px rgba(0,0,0,.45);
  }
  .card--back { left: 45px; }
  .card--front { left: 635px; }

  .company-name {
    position: absolute;
    display: flex;
    align-items: center;
    gap: 10px;
    font-size: 30px;
    line-height: 1;
    font-weight: 600;
    letter-spacing: 1px;
  }
  .company-name__square {
    width: 14px; height: 14px;
    background: currentColor;
  }

  /* back */
  .card--back .company-name {
    right: 40px; top: 60px;
    color: var(--name-faint);
  }
  .members {
    position: absolute;
    left: 34px; top: 150px;
    font-size: 11.5px; line-height: 1.6;
    color: var(--ink-soft);
  }
  .members__title {
    font-weight: 700; color: var(--ink);
    text-decoration: underline; letter-spacing: .3px;
  }

  /* front */
  .person { position: absolute; left: 34px; top: 34px; }
  .person__name { font-weight: 700; font-size: 15px; letter-spacing: .8px; text-transform: uppercase; }
  .person__role { font-size: 11px; color: var(--ink-soft); }
  .card--front .company-name {
    right: 40px; top: 150px;
    color: var(--name-silver);
  }
  .contact {
    position: absolute;
    left: 34px; bottom: 30px;
    font-size: 11.5px; line-height: 1.6;
    color: var(--ink-soft);
  }
  .contact__web { font-weight: 700; color: var(--ink); }
  .contact__company { font-weight: 700; color: var(--ink); text-decoration: underline; text-transform: uppercase; letter-spacing: .3px; }
  .contact__filing { font-weight: 700; color: var(--ink); }
</style>
</head>
<body>
  <section class="card card--back" aria-label="Back of business card">
    <div class="company-name"><span class="company-name__square"></span>Brass Lark</div>
    <div class="members">
      <p class="members__title">PROUD GROUP MEMBERS:</p>
      <p>UK: Marrow Bay Associates Ltd. | 42 Elmsworth Row, 1st fl. | W1T-4QR London</p>
      <p>PL: Marrow Bay Trust S.A. | ul. Lipowa Polna 14, 4p. | 00-871 Warszawa</p>
      <p>US: Crestfall Advisors, LLC | 213 Orchard Lane, Suite 409, NYC | 10017 New York</p>
    </div>
  </section>

  <section class="card card--front" aria-label="Front of business card">
    <div class="person">
      <p class="person__name">Wiktor Osmalek</p>
      <p class="person__role">President &amp; CEO</p>
    </div>
    <div class="company-name"><span class="company-name__square"></span>Brass Lark</div>
    <div class="contact">
      <p class="contact__web">www.brlcap.example</p>
      <p class="contact__company">Brass Lark Venture Capital, LLC</p>
      <p>P: +44 20 7395 2847 &nbsp;|&nbsp; M: +44 75 2918 3406 &nbsp;|&nbsp; vik@brlcap.example</p>
      <p>17 W Pinecrest Ave., Sheridan, WY 82801 &nbsp;|&nbsp; <span class="contact__filing">Filling number: 2019-000542319</span></p>
    </div>
  </section>
</body>
</html>
```